Business Card & Logo Design Project

I am looking for a slick/simple design for a logo and business card, for a music Producer/Mixer/Engineer.

I'm based in Tokyo, Japan and I help my clients polish up their creation to major radio/TV status. My clients pay me for my taste, sense of balance expertise and creative direction/

Design should give impression of seal of quality, professionalism, and enthusiasm need some sort of a logo like design for "vantrix productions".

Please don't include music notes or instruments or anything musically related and anything samurai or ninja or too much Japan in them on the design.

I like clever, slick stuff that's not too obvious.
I also like a smooth gradation type transition. My favorite color is deep dark blue/

Good Luck and Thank you for your effort.
Updates

I would like a two-sided design for this one.
One side with "vantrix productions" (all lower case) on, and the other side with my name and contact info.

Please also consider portrait position (or direction).  (as opposed to landscape) 

Target Market(s)

My primary targets are artists & bands, who want absolute best for their creation.

Industry/Entity Type

Business

Requirements
Must have
• Two-Sided
1, vantrix productions
2, Kenji Harumoto, Producer/Mixer/Engineer, +81 090 4827 3516, brambleway@mailnest.example
Nice to have
• Any suggestions are welcome//
Should not have
• Anything music related images.
(e.g. CD, music notations, instruments etc.)

```html
<!DOCTYPE html>
<html lang="en">
<head>
<meta charset="utf-8">
<title>vantrix productions – business card</title>
<link rel="stylesheet" href="https://fonts.googleapis.com/css2?family=Questrial&family=Nunito+Sans:wght@800&display=swap">
<style>
  :root {
    --page: #ffffff;
    --blue-deep: #03507f;
    --blue-mid: #0a67a0;
    --blue-dark: #0a3f66;
    --red: #b81f2d;
    --red-dark: #8e1320;
    --band: rgba(238, 178, 184, 0.62);
    --ink: #1c1a1b;
    --white: #ffffff;
  }
  html, body {
    margin: 0;
    width: 1200px;
    height: 1000px;
    overflow: hidden;
    background: var(--page);
  }
  .canvas {
    position: relative;
    width: 1200px;
    height: 1000px;
  }
  .card {
    position: absolute;
    top: 25px;
    width: 526px;
    height: 948px;
    box-shadow: 0 2px 6px rgba(0,0,0,0.35);
  }
  .card--front { left: 37px; }
  .card--back { left: 637px; }
  .card svg { display: block; width: 100%; height: 100%; }
  .wordmark {
    font-family: "Questrial", "Century Gothic", sans-serif;
    font-size: 74px;
  }
  .wordmark--top { fill: var(--ink); }
  .wordmark--bottom { fill: var(--white); }
  .center-name {
    font-family: "Questrial", "Century Gothic", sans-serif;
    font-size: 40px;
    fill: var(--ink);
  }
  .contact {
    font-family: "Nunito Sans", "Avenir", sans-serif;
    font-weight: 800;
    fill: var(--ink);
  }
  .contact__name { font-size: 50px; }
  .contact__line { font-size: 29px; }
  .contact__email { font-size: 27px; }
</style>
</head>
<body>
<div class="canvas">

  <div class="card card--front">
    <svg viewBox="0 0 526 948" aria-labelledby="front-title">
      <title id="front-title">vantrix productions</title>
      <defs>
        <radialGradient id="front-art" cx="0.52" cy="0.5" r="0.62">
          <stop offset="0" stop-color="#c42433"/>
          <stop offset="0.55" stop-color="var(--red-dark)"/>
          <stop offset="1" stop-color="var(--blue-dark)"/>
        </radialGradient>
        <filter id="edge-shadow" x="-10%" y="-10%" width="120%" height="130%">
          <feDropShadow dx="0" dy="6" stdDeviation="7" flood-color="#000" flood-opacity="0.55"/>
        </filter>
        <filter id="edge-shadow-up" x="-10%" y="-30%" width="120%" height="130%">
          <feDropShadow dx="0" dy="-6" stdDeviation="7" flood-color="#000" flood-opacity="0.55"/>
        </filter>
      </defs>
      <rect class="card__artwork" width="526" height="948" fill="url(#front-art)" role="img" aria-label="Abstract red concentric ring artwork on deep blue"/>
      <rect class="card__band" x="0" y="360" width="526" height="230" fill="var(--band)"/>
      <polygon class="card__corner-top" points="0,0 526,0 526,360" fill="var(--blue-deep)" filter="url(#edge-shadow)"/>
      <polygon class="card__corner-bottom" points="0,590 526,948 0,948" fill="var(--blue-mid)" filter="url(#edge-shadow-up)"/>
      <text class="wordmark wordmark--top" x="305" y="175" text-anchor="middle" transform="rotate(34.4 305 160)">vantrix</text>
      <text class="wordmark wordmark--bottom" x="215" y="830" text-anchor="middle" transform="rotate(34.4 215 810)">productions</text>
      <text class="center-name" x="263" y="488" text-anchor="middle">vantrix</text>
    </svg>
  </div>

  <div class="card card--back">
    <svg viewBox="0 0 526 948" aria-labelledby="back-title">
      <title id="back-title">Kenji Harumoto contact details</title>
      <defs>
        <radialGradient id="back-art" cx="0.3" cy="0.35" r="0.85">
          <stop offset="0" stop-color="#c5222f"/>
          <stop offset="1" stop-color="var(--red-dark)"/>
        </radialGradient>
        <filter id="back-shadow" x="-10%" y="-10%" width="120%" height="130%">
          <feDropShadow dx="0" dy="6" stdDeviation="7" flood-color="#000" flood-opacity="0.55"/>
        </filter>
        <filter id="back-shadow-up" x="-10%" y="-30%" width="120%" height="130%">
          <feDropShadow dx="0" dy="-6" stdDeviation="7" flood-color="#000" flood-opacity="0.55"/>
        </filter>
      </defs>
      <rect class="card__artwork" width="526" height="948" fill="url(#back-art)" role="img" aria-label="Abstract red concentric ring artwork"/>
      <rect class="card__band" x="0" y="360" width="526" height="230" fill="var(--band)"/>
      <polygon class="card__corner-top" points="0,0 526,0 526,360" fill="var(--blue-deep)" filter="url(#back-shadow)"/>
      <polygon class="card__corner-bottom" points="0,590 526,948 0,948" fill="var(--blue-mid)" filter="url(#back-shadow-up)"/>
      <text class="wordmark wordmark--top" x="305" y="175" text-anchor="middle" transform="rotate(34.4 305 160)">vantrix</text>
      <text class="wordmark wordmark--bottom" x="215" y="830" text-anchor="middle" transform="rotate(34.4 215 810)">productions</text>
      <g class="contact">
        <text class="contact__name" x="43" y="430">Kenji Harumoto</text>
        <text class="contact__line" x="43" y="472">Producer/Mixer/Engineer</text>
        <text class="contact__line" x="43" y="515">+81 090 4827 3516</text>
        <text class="contact__email" x="43" y="558">brambleway@mailnest.example</text>
      </g>
    </svg>
  </div>

</div>
</body>
</html>
```